Breast Cancer Stickers

Hi,
i would like a of small design for a breast cancer awareness campaign. please check attached picture this is the size and font i want. these will be stickers. Then i would like a little pink ribbon after each dot. so there will be four design please find below colors, slogans, etc..
1 I PINK I CAN. (Off white Background, Light Pink Font)
Never give up.
2 PINK POWER. (Black Background, Bright Pink Font)
Theres Always hope
3 POSITIVELY PINK. ( Light Pink Background, Off white Font)
Stay Positive
4 TURN UP THE PINK. (Bright Pink Background, Black font)
fight on.
Campaign

```html
<!DOCTYPE html>
<html lang="en">
<head>
<meta charset="utf-8">
<title>Breast Cancer Awareness Stickers</title>
<link rel="stylesheet" href="https://fonts.googleapis.com/css2?family=Inter:wght@700&display=swap">
<style>
  :root {
    --stage: #322429;
    --off-white: #ffffff;
    --black: #000000;
    --light-pink: #ffa0c8;
    --bright-pink: #ff1f69;
  }
  html, body {
    margin: 0;
    padding: 0;
    width: 1200px;
    height: 1000px;
    overflow: hidden;
    background: var(--stage);
  }
  .sheet {
    position: relative;
    width: 1200px;
    height: 1000px;
    font-family: "Inter", "Helvetica Neue", Arial, sans-serif;
    font-weight: 700;
  }
  .sticker {
    position: absolute;
    top: 376px;
    width: 250px;
    height: 250px;
  }
  .sticker--pink-can { left: 69px; background: var(--off-white); color: var(--light-pink); --ribbon: var(--bright-pink); --pad: 37px; }
  .sticker--power { left: 340px; background: var(--black); color: var(--bright-pink); --ribbon: var(--light-pink); --pad: 34px; }
  .sticker--positive { left: 612px; background: var(--light-pink); color: var(--off-white); --ribbon: var(--bright-pink); --pad: 25px; }
  .sticker--turn-up { left: 883px; background: var(--bright-pink); color: var(--black); --ribbon: var(--light-pink); --pad: 34px; }

  .slogan {
    position: absolute;
    left: var(--pad);
    top: 75px;
    margin: 0;
    font-size: 45px;
    line-height: 42px;
    letter-spacing: -1px;
    white-space: nowrap;
    font-weight: 700;
  }
  .tagline {
    position: absolute;
    left: var(--pad);
    top: 164px;
    margin: 0;
    font-size: 17px;
    line-height: 20px;
    letter-spacing: -0.2px;
    white-space: nowrap;
  }
  .ribbon {
    display: inline-block;
    width: 10px;
    height: 16px;
    margin-left: 2px;
    vertical-align: -7px;
  }
  .ribbon path {
    fill: none;
    stroke: var(--ribbon);
    stroke-width: 2;
    stroke-linecap: round;
  }
</style>
</head>
<body>
<main class="sheet">
  <section class="sticker sticker--pink-can">
    <h2 class="slogan">I Pink<br>I Can<svg class="ribbon" viewBox="0 0 10 16" aria-hidden="true"><path d="M3 9 C1 6 2 1.5 5 1.5 C8 1.5 9 6 7 9 L3 15 M3 9 L7 15"/></svg></h2>
    <p class="tagline">Never Give Up</p>
  </section>
  <section class="sticker sticker--power">
    <h2 class="slogan">Pink<br>Power<svg class="ribbon" viewBox="0 0 10 16" aria-hidden="true"><path d="M3 9 C1 6 2 1.5 5 1.5 C8 1.5 9 6 7 9 L3 15 M3 9 L7 15"/></svg></h2>
    <p class="tagline">Theres Always Hope</p>
  </section>
  <section class="sticker sticker--positive">
    <h2 class="slogan">Positively<br>Pink<svg class="ribbon" viewBox="0 0 10 16" aria-hidden="true"><path d="M3 9 C1 6 2 1.5 5 1.5 C8 1.5 9 6 7 9 L3 15 M3 9 L7 15"/></svg></h2>
    <p class="tagline">Stay Positive</p>
  </section>
  <section class="sticker sticker--turn-up">
    <h2 class="slogan">Turn Up<br>the Pink<svg class="ribbon" viewBox="0 0 10 16" aria-hidden="true"><path d="M3 9 C1 6 2 1.5 5 1.5 C8 1.5 9 6 7 9 L3 15 M3 9 L7 15"/></svg></h2>
    <p class="tagline">Fight On</p>
  </section>
</main>
</body>
</html>
```